Cleaning service website design

We need a new nice web design(logo will be the same) for a new cleaning service Company:

Informations about Company and logo you can take from flyers in attachments.

This is a cleaning service Company which have simple rules and we would like to show that(in checklist form) on website:

- What we do and that we're Cleaning Green

- Why us?

- How much(our pricing is simple)

Also we would like to communicate with clients by some nice/big pictures on website and the most important thing is our phone number and short/fast Freestimate.

Also there should be some space for description about our Company.

Generally all information on main page can be short: about us, about service(what we do), last reviews, tips (for example: Tip of the week) and other can be some introduction to subpage where will be more information.

There will be few subpages like: About us, About our service, Photos(Before and after), Reviews , Tips, FAQ, Contact, Looking for a Job? - most of them will be just text so you can project just one example.

```html
<!DOCTYPE html>
<html lang="en">
<head>
<meta charset="utf-8">
<title>Tidy Nest House Cleaning</title>
<link rel="stylesheet" href="https://fonts.googleapis.com/css2?family=Open+Sans:ital,wght@0,400;0,600;0,700;1,700&display=swap">
<style>
  :root {
    --blue: #0a5aa8;
    --blue-line: #3f7fc0;
    --green: #6cc067;
    --white: #ffffff;
    --photo-light: #e9e4dc;
    --photo-warm: #b89a78;
    --photo-blue: #2f4fa8;
  }
  * { margin: 0; padding: 0; box-sizing: border-box; }
  html, body { width: 1200px; height: 1200px; overflow: hidden; background: var(--white); }
  body { font-family: "Open Sans", Arial, sans-serif; }
  .page { position: relative; width: 1200px; height: 1200px; overflow: hidden; }

  .site-title {
    position: absolute; left: 42px; top: 10px;
    font-size: 36px; font-style: italic; font-weight: 700; color: var(--green);
    letter-spacing: -0.5px;
  }
  .call {
    position: absolute; left: 762px; top: 8px; display: flex; align-items: center; gap: 10px;
    font-size: 36px; font-style: italic; font-weight: 700; color: var(--green);
  }
  .call svg { width: 30px; height: 44px; }

  .main-nav { position: absolute; left: 0; top: 72px; width: 1200px; height: 60px; display: flex; gap: 2px; background: var(--blue-line); }
  .main-nav a {
    flex: 1; display: flex; align-items: center; justify-content: center;
    background: var(--blue); color: var(--white); text-decoration: none;
    font-size: 36px; font-style: italic; font-weight: 700; letter-spacing: -0.5px;
  }
  .main-nav a.is-open { background: var(--green); }

  .dropdown { position: absolute; left: 960px; top: 132px; width: 240px; z-index: 3; display: flex; flex-direction: column; gap: 2px; }
  .dropdown a {
    display: flex; align-items: center; height: 60px; padding-left: 70px;
    background: var(--blue); color: var(--white); text-decoration: none;
    font-size: 36px; font-style: italic; font-weight: 700; letter-spacing: -0.5px;
  }
  .dropdown a.alt { background: var(--green); }

  .hero {
    position: absolute; left: 0; top: 144px; width: 1200px; height: 456px;
    background: linear-gradient(90deg, var(--photo-light) 0%, var(--photo-warm) 20%, var(--photo-light) 30%, var(--photo-blue) 42%, var(--photo-blue) 62%, var(--photo-light) 72%, var(--photo-warm) 88%, var(--photo-light) 100%);
  }
  .price-ribbon { position: absolute; left: 0; top: 144px; width: 290px; height: 190px; z-index: 2; }
  .brand-mark {
    position: absolute; left: 1000px; top: 510px; z-index: 2;
    display: flex; align-items: center; gap: 8px;
    font-size: 24px; font-weight: 700; color: var(--white);
  }
  .brand-mark .dot { width: 22px; height: 22px; border-radius: 50%; background: var(--green); }

  .estimate-band { position: absolute; left: 0; top: 614px; width: 1200px; height: 88px; }
  .estimate-band svg { position: absolute; left: 0; top: 0; }
  .estimate-label {
    position: absolute; left: 40px; top: 0; height: 88px; line-height: 88px;
    font-size: 48px; font-weight: 600; color: var(--white);
  }
  .estimate-offer {
    position: absolute; left: 440px; top: 0; height: 88px; line-height: 88px;
    font-size: 48px; font-style: italic; font-weight: 700; color: var(--green); letter-spacing: -0.5px;
  }

  .info-box {
    position: absolute; top: 718px; height: 406px; background: var(--blue);
    color: var(--white); font-size: 23px; font-weight: 600; line-height: 43px;
    padding: 22px 14px 0 16px;
  }
  .info-box ul { list-style: none; }
  .info-box .hang { padding-left: 14px; text-indent: -14px; }
  .why-us { left: 43px; width: 364px; }
  .what-we-do { left: 421px; width: 363px; }
  .about-blurb { left: 798px; width: 363px; padding-left: 32px; }

  .footer {
    position: absolute; left: 0; top: 1152px; width: 1200px; text-align: center;
    font-size: 14px; color: var(--green);
  }
</style>
</head>
<body>
<div class="page">
  <header>
    <div class="site-title">Housecleaning...Tidy Nest</div>
    <div class="call">
      <svg viewBox="0 0 30 44" aria-hidden="true">
        <rect x="6" y="2" width="20" height="38" rx="4" transform="rotate(12 16 21)" fill="none" stroke="#0a5aa8" stroke-width="3"/>
      </svg>
      <span>Call: 289-555-0142</span>
    </div>
  </header>

  <nav class="main-nav">
    <a href="#">About us</a>
    <a href="#">Services</a>
    <a href="#">Reviews</a>
    <a href="#">Tips</a>
    <a href="#" class="is-open">More</a>
  </nav>
  <nav class="dropdown">
    <a href="#">Photos</a>
    <a href="#" class="alt">FAQ</a>
    <a href="#">Contact</a>
    <a href="#" style="height:64px">Jobs</a>
  </nav>

  <div class="hero" role="img" aria-label="Photo of a cleaner in a blue top and yellow rubber gloves, hands on hips, holding a cloth and spray bottle in a bright kitchen"></div>

  <svg class="price-ribbon" viewBox="0 0 290 190" aria-label="from 79$">
    <polygon points="0,0 282,0 0,186" fill="#0a5aa8"/>
    <text x="20" y="140" transform="rotate(-33 20 140)" fill="#ffffff" font-family="Open Sans, Arial, sans-serif" font-style="italic" font-weight="700">
      <tspan font-size="28">from </tspan><tspan font-size="50">79$</tspan>
    </text>
  </svg>

  <div class="brand-mark"><span class="dot"></span><span>Tidy Nest</span></div>

  <section class="estimate-band">
    <svg width="410" height="88" viewBox="0 0 410 88" aria-hidden="true">
      <polygon points="0,0 384,0 406,44 384,88 0,88" fill="#0a5aa8"/>
    </svg>
    <div class="estimate-label">Free estimate</div>
    <div class="estimate-offer">Ask for a free price offer!</div>
  </section>

  <section class="info-box why-us">
    <ul>
      <li>- Locally Owned &amp; Operated</li>
      <li>- Reliable &amp; Affordable</li>
      <li>- All Supplies Provided</li>
      <li>- Green Cleaning</li>
      <li>- Pet Friendly</li>
      <li>- No Contracts</li>
    </ul>
  </section>

  <section class="info-box what-we-do">
    <ul>
      <li class="hang">-Thoroughly clean your bathrooms, kitchen, bedrooms and living areas</li>
      <li>- Mop or vacuum your floor</li>
      <li>- Dust surfaces</li>
      <li>- Collect garbage</li>
      <li>- Make beds</li>
    </ul>
  </section>

  <section class="info-box about-blurb">
    <p>Have you ever wondered what it would be<br>like if your life was more simple? We’re here to help by taking over the chores of house cleaning.</p>
  </section>

  <footer class="footer">© 2012 Tidy Nest House Cleaning. All rights reserved.</footer>
</div>
</body>
</html>
```